Ferncrest Dental, LLC business card project

Business card to be designed with current logo.
Dental office- please keep design of card that looks clean and professional.
Please include the following info:
Ferncrest Dental, LLC
Dr. Lorna Pettigrew
2871 Marlowe Street
Millbrook, OR 97093
541-555-0193
ferncrestdental.office@examplemail.test
Hello everyone-
Reason: Just got back from overseas- will look at all designs and provide feedback. Thank you!
Reason: Polling my friends for the final selection-
thank you to all those that participated- so many talented designers!

```html
<!DOCTYPE html>
<html lang="en">
<head>
<meta charset="utf-8">
<title>Ferncrest Dental, LLC – Business Cards</title>
<link href="https://fonts.googleapis.com/css2?family=Crimson+Pro:wght@400;600;700&display=swap" rel="stylesheet">
<style>
  :root {
    --page: #f1f1f1;
    --green-light: #97c03b;
    --green-mid: #6ea534;
    --green-deep: #4f8c2d;
    --band: #4c8a31;
    --paper: #f2f2f2;
    --paper-edge: #dcdcdc;
    --ink-light: #ffffff;
    --cell: #d9e7c4;
    --brand: #76ab35;
  }
  * { box-sizing: border-box; margin: 0; padding: 0; }
  html, body { width: 1200px; height: 1013px; overflow: hidden; }
  body {
    background: var(--page);
    font-family: "Crimson Pro", Georgia, serif;
    position: relative;
  }
  .card {
    position: absolute;
    width: 392px;
    height: 650px;
    display: flex;
    flex-direction: column;
    background: var(--paper);
    box-shadow: 0 6px 18px rgba(0,0,0,0.2);
  }
  .card--front { left: 192px; top: 186px; }
  .card--back  { left: 678px; top: 156px; }

  .card__top {
    height: 360px;
    flex: none;
    background: radial-gradient(ellipse at 0% 0%, var(--green-light) 0%, var(--green-mid) 45%, var(--green-deep) 100%);
    color: var(--ink-light);
    position: relative;
  }
  .card--back .card__top { height: 354px; }
  .card__middle {
    flex: 1;
    background: linear-gradient(180deg, var(--paper-edge) 0%, var(--paper) 14%, #ffffff 50%, var(--paper) 100%);
    display: flex;
    align-items: center;
    justify-content: center;
  }
  .card__band {
    height: 64px;
    flex: none;
    background: var(--band);
    color: var(--ink-light);
    display: flex;
    align-items: center;
    justify-content: center;
    font-size: 19px;
  }
  .card--back .card__band { height: 74px; }

  /* Front contact block */
  .contact { padding: 70px 0 0 38px; }
  .contact__company { font-size: 28px; font-weight: 700; margin-bottom: 14px; }
  .contact__row { display: flex; align-items: flex-start; }
  .contact__icon { width: 28px; height: 28px; margin-right: 20px; margin-top: 4px; flex: none; }
  .contact__lines { font-size: 25px; line-height: 1.28; }
  .contact__row--phone { margin-top: 26px; align-items: center; }
  .contact__row--phone .contact__icon { margin-top: 0; }

  /* Brand name */
  .brand { display: flex; align-items: center; gap: 10px; }
  .brand__dot { width: 14px; height: 14px; border-radius: 50%; background: var(--brand); }
  .brand__name { color: var(--brand); font-size: 31px; font-weight: 400; white-space: nowrap; }

  /* Appointment table */
  .appointments { padding-top: 30px; }
  .appointments__title { text-align: center; font-size: 31px; font-weight: 700; margin-bottom: 10px; }
  .appointments__table { margin-left: 38px; border-collapse: separate; border-spacing: 0 5px; }
  .appointments__table th { font-size: 18px; font-weight: 700; text-align: left; height: 18px; }
  .appointments__table th.date { padding-left: 24px; }
  .appointments__table th.note { padding-left: 22px; }
  .appointments__table td { background: var(--cell); height: 32px; }
  .appointments__table td.date { width: 93px; }
  .appointments__table td.note { width: 212px; border-left: 9px solid var(--green-mid); background-clip: padding-box; }
</style>
</head>
<body>

  <section class="card card--front" aria-label="Business card front">
    <div class="card__top">
      <div class="contact">
        <h1 class="contact__company">Ferncrest Dental, LLC</h1>
        <div class="contact__row">
          <svg class="contact__icon" viewBox="0 0 30 30" aria-hidden="true">
            <circle cx="15" cy="9" r="7" fill="#fff"/>
            <path d="M2 29 C3 19 8 17 15 17 C22 17 27 19 28 29 Z" fill="#fff"/>
            <path d="M13 17 L15 24 L17 17 Z" fill="#6ea534"/>
          </svg>
          <div class="contact__lines">
            <p>Dr. Lorna Pettigrew</p>
            <p>2871 Marlowe Street</p>
            <p>Millbrook, OR 97093</p>
          </div>
        </div>
        <div class="contact__row contact__row--phone">
          <svg class="contact__icon" viewBox="0 0 30 30" aria-hidden="true">
            <path d="M8 3 C5 4 3 7 4 11 C6 18 12 24 19 27 C23 28 26 26 27 23 L22 18 L18 21 C14 19 11 16 9 12 L12 8 Z" fill="#fff"/>
          </svg>
          <p class="contact__lines">541-555-0193</p>
        </div>
      </div>
    </div>
    <div class="card__middle">
      <div class="brand">
        <span class="brand__dot" aria-hidden="true"></span>
        <span class="brand__name">Ferncrest Dental, LLC</span>
      </div>
    </div>
    <div class="card__band">ferncrestdental.office@examplemail.test</div>
  </section>

  <section class="card card--back" aria-label="Business card back">
    <div class="card__top appointments">
      <h2 class="appointments__title">Appointments</h2>
      <table class="appointments__table">
        <thead>
          <tr><th class="date">Date</th><th class="note">Note</th></tr>
        </thead>
        <tbody>
          <tr><td class="date"></td><td class="note"></td></tr>
          <tr><td class="date"></td><td class="note"></td></tr>
          <tr><td class="date"></td><td class="note"></td></tr>
          <tr><td class="date"></td><td class="note"></td></tr>
          <tr><td class="date"></td><td class="note"></td></tr>
          <tr><td class="date"></td><td class="note"></td></tr>
        </tbody>
      </table>
    </div>
    <div class="card__middle">
      <div class="brand">
        <span class="brand__dot" aria-hidden="true"></span>
        <span class="brand__name">Ferncrest Dental, LLC</span>
      </div>
    </div>
    <div class="card__band">ferncrestdental.office@examplemail.test</div>
  </section>

</body>
</html>
```